Sticker mit Text
Zielgruppe
Buchverkauf
Aufgabenstellung
Das Design soll als Sticker in Pakete geklebt werden. Hierfür verwenden wir Die Cut Sticker von Klebfuchs in einer Formatgröße von etwa 10x10cm. https://www.klebfuchs-example.com/products/die-cut-stickers
Auf dem Sticker soll folgender Text enthalten sein:
Haben Sie es gewusst? Es gibt nur 4 giftige Vogelarten.
Der Pitohui ist einer von ihnen. Er ist giftig, weil er giftige Käfer frisst. Je mehr er davon verspeist, desto giftiger wird er.
Was manche Käufer bei Warholt vielleicht auch nicht wissen, dass sich ein Verkäufer prima durch eine Sterne-Bewertung unterstützen lässt. Probieren Sie es aus. Wenden Sie hierfür vorsichtig die Feder des Pitohui!
Von der Umrandung des Stickers sollte man einen Vogel erkennen können. Ggf. lässt sich ein Vogel aber auch in den Sticker integrieren.

```html
<!DOCTYPE html>
<html lang="de">
<head>
<meta charset="utf-8">
<title>Pitohui Sticker – Sterne-Bewertung</title>
<link rel="stylesheet" href="https://fonts.googleapis.com/css2?family=Anton&family=Roboto+Condensed:wght@500;700&display=swap">
<style>
  :root {
    --bg: #ececea;
    --star-yellow: #f6b912;
    --sticker-white: #ffffff;
    --ink: #141414;
    --accent-orange: #ef7b12;
    --bird-dark: #1c1c1c;
  }
  * { box-sizing: border-box; margin: 0; padding: 0; }
  html, body { width: 848px; height: 1200px; overflow: hidden; }
  body { background: var(--bg); position: relative; font-family: "Roboto Condensed", sans-serif; }

  .sticker { position: absolute; left: 74px; top: 240px; width: 700px; height: 680px; }
  .sticker-shape { position: absolute; inset: 0; filter: drop-shadow(0 2px 3px rgba(0,0,0,.25)); }

  .bird-illustration {
    position: absolute; left: 58px; top: 78px; width: 250px; height: 230px;
    background: var(--bird-dark);
    border-radius: 48% 52% 46% 54% / 55% 50% 50% 45%;
    border: 10px solid var(--sticker-white);
  }

  .sticker-copy {
    position: absolute; left: 150px; top: 290px; width: 470px;
    display: flex; flex-direction: column; align-items: center;
    transform: rotate(-5deg); color: var(--ink); text-align: center;
  }
  .bar {
    background: var(--ink); font-family: "Anton", sans-serif;
    color: var(--accent-orange); text-transform: uppercase;
    line-height: 1.1; padding: 2px 10px; letter-spacing: .5px;
  }
  .headline { font-size: 28px; align-self: flex-end; margin-right: 10px; margin-bottom: 6px; }
  .body-text { font-size: 18px; font-weight: 500; line-height: 1.2; }
  .body-text + .body-text { margin-top: 14px; }
  .claim { margin-top: 6px; display: flex; flex-direction: column; align-items: center; }
  .claim-small { font-size: 22px; align-self: flex-start; }
  .claim-large { font-size: 36px; margin-left: 40px; }
  .claim-mid { font-size: 34px; align-self: flex-start; margin-left: 10px; }
  .call-to-action {
    margin-top: 4px; background: var(--ink); color: var(--sticker-white);
    font-size: 17px; font-weight: 700; line-height: 1.2; padding: 4px 14px;
    margin-left: 60px;
  }
</style>
</head>
<body>
  <div class="sticker">
    <svg class="sticker-shape" viewBox="0 0 700 680" width="700" height="680" aria-hidden="true">
      <polygon points="350,20 438.2,248.6 682.9,261.8 492.7,416.4 555.7,653.2 350,520 144.3,653.2 207.3,416.4 17.1,261.8 261.8,248.6"
               fill="var(--sticker-white)" stroke="var(--sticker-white)" stroke-width="34" stroke-linejoin="miter"/>
      <polygon points="350,20 438.2,248.6 682.9,261.8 492.7,416.4 555.7,653.2 350,520 144.3,653.2 207.3,416.4 17.1,261.8 261.8,248.6"
               fill="var(--star-yellow)"/>
    </svg>

    <div class="bird-illustration" role="img" aria-label="Illustration: schwarzer Pitohui-Vogel mit orangem Flügel und Auge, auf dem Stern sitzend"></div>

    <div class="sticker-copy">
      <div class="bar headline">Haben Sie es gewusst?</div>
      <p class="body-text">Es gibt nur 4 giftige Vogelarten. Der Pitohui ist einer<br>von ihnen. Er ist giftig, weil er giftige Käfer frisst. Je mehr<br>er davon verspeist, desto giftiger wird er.</p>
      <p class="body-text">Was manche Käufer<br>bei Warholt vielleicht auch nicht wissen,</p>
      <div class="claim">
        <div class="bar claim-small">dass sich ein Verkäufer prima durch</div>
        <div class="bar claim-large">eine Sterne-Bewertung</div>
        <div class="bar claim-mid">unterstützen lässt.</div>
      </div>
      <p class="call-to-action">Probieren Sie es aus. Wenden Sie hierfür<br>vorsichtig die Feder des Pitohui!</p>
    </div>
  </div>
</body>
</html>
```